Business cards for investing fund

I need processional luxury classical business cards for CEO of the investing company. I need it to be elegant. I need it to look expensive. It will be printed o fine paper with UV. I prefer light and minimalistic design. Logo of my company must be included at least on front page.

Target Market(s)

40+ investors

Industry/Entity Type

Finance And Accounting

Contact Information for Business Card

FRONT PAGE:

Wiktor Osmalek
President & CEO

e: vik@brlcap.example
w: www.brlcap.example
p: +44 20 7395 2847
m: +44 75 2918 3406

Brass Lark Venture Capital, LLC
17 W Pinecrest Ave., Sheridan, WY 82801
Filling number: 2019-000542319

BACK PAGE (with or without logo):

PROUD GROUP MEMBERS:

UK: Marrow Bay Associates Ltd. | 42 Elmsworth Row, 1st fl. | W1T-4QR London
PL: Marrow Bay Trust S.A. | ul. Lipowa Polna 14, 4p. | 00-871 Warszawa
US: Crestfall Advisors, LLC | 213 Orchard Lane, Suite 409, NYC | 10017 New York

Font styles to use
Serif
Sans Serif
Decorative

Colors
0355a3
ec1f27

Requirements
Must have
• My own logo (attached)

```html
<!DOCTYPE html>
<html lang="en">
<head>
<meta charset="utf-8">
<title>Brass Lark Venture Capital – Business Cards</title>
<link href="https://fonts.googleapis.com/css2?family=PT+Serif:wght@400;700&display=swap" rel="stylesheet">
<style>
  :root{
    --backdrop:#5a3a1e;
    --card:#121212;
    --card-gloss:#1e1e1e;
    --text:#a9a9a9;
    --text-bright:#d6d6d6;
    --logo:#b8b8b8;
  }
  *{margin:0;padding:0;box-sizing:border-box}
  html,body{width:1200px;height:886px;overflow:hidden}
  body{
    background:var(--backdrop);
    font-family:"PT Serif",Georgia,serif;
    position:relative;
  }
  .card{
    position:absolute;
    width:540px;height:309px;
    background:var(--card);
    color:var(--text);
    box-shadow:0 14px 30px rgba(0,0,0,.45);
    overflow:hidden;
  }
  .card--back{left:40px;top:90px;background:linear-gradient(160deg,var(--card-gloss),var(--card) 60%)}
  .card--front{left:620px;top:480px}

  /* shared logo lettering */
  .logo-mark{
    position:absolute;right:28px;text-align:right;
    font-weight:400;color:var(--logo);text-transform:uppercase;line-height:1.05;
  }
  .logo-mark__name{display:block;letter-spacing:1px}
  .logo-mark__sub{display:block;letter-spacing:.5px}

  /* back */
  .group-title{
    position:absolute;left:70px;top:32px;
    font-size:14px;font-weight:400;letter-spacing:.5px;
    text-decoration:underline;text-underline-offset:3px;
    color:var(--text-bright);
  }
  .member{position:absolute;font-size:14px;line-height:1.45}
  .member--pl{left:330px;top:28px}
  .member--uk{left:34px;top:108px}
  .member--us{left:170px;top:215px}
  .card--back .logo-mark{top:130px}
  .card--back .logo-mark__name{font-size:26px}
  .card--back .logo-mark__sub{font-size:11px;margin-top:3px}

  /* front */
  .card--front .logo-mark{top:26px}
  .card--front .logo-mark__name{font-size:40px}
  .card--front .logo-mark__sub{font-size:16px;margin-top:4px}
  .filing{position:absolute;right:28px;top:100px;font-size:12px}
  .person{position:absolute;left:34px;top:120px}
  .person__name{font-size:20px;font-weight:700;color:var(--text-bright);letter-spacing:.5px;line-height:1.2}
  .person__role{font-size:13px;margin-top:2px}
  .address{position:absolute;left:56px;top:180px;font-size:13px;line-height:1.35}
  .contacts{position:absolute;left:56px;top:220px;list-style:none;font-size:13px;line-height:1.5}
  .contacts li{display:flex;align-items:center;gap:8px}
  .contacts svg{width:11px;height:11px;fill:none;stroke:var(--text);stroke-width:1.3;flex:none}
</style>
</head>
<body>

<section class="card card--back" aria-label="Business card, back">
  <h2 class="group-title">PROUD GROUP MEMBERS:</h2>
  <p class="member member--pl">Marrow Bay Trust S.A.<br>ul. Lipowa Polna 14,<br>4p 00-871 Warszawa</p>
  <p class="member member--uk">Marrow Bay Associates Ltd.<br>42 Elmsworth Row, 1st fl.<br>W1T-4QR London</p>
  <p class="member member--us">Crestfall Advisors, LLC<br>213 Orchard Lane, Suite 409,<br>NYC 10017 New York</p>
  <div class="logo-mark"><span class="logo-mark__name">Brass Lark</span><span class="logo-mark__sub">Venture Capital, LLC</span></div>
</section>

<section class="card card--front" aria-label="Business card, front">
  <div class="logo-mark"><span class="logo-mark__name">Brass Lark</span><span class="logo-mark__sub">Venture Capital, LLC</span></div>
  <p class="filing">Filling number: 2019-000542319</p>

  <div class="person">
    <h1 class="person__name">Wiktor Osmalek</h1>
    <p class="person__role">President &amp; CEO</p>
  </div>

  <p class="address">17 W Pinecrest Ave.,<br>Sheridan, WY 82801</p>

  <ul class="contacts">
    <li><svg viewBox="0 0 12 12"><rect x="3" y="1" width="6" height="10" rx="1"/></svg>+44 75 2918 3406</li>
    <li><svg viewBox="0 0 12 12"><path d="M2 2c1-1 2-1 2.5 0l1 2-1 1c.5 1.2 1.3 2 2.5 2.5l1-1 2 1c1 .5 1 1.5 0 2.5C7 11 1 5 2 2z"/></svg>+44 20 7395 2847</li>
    <li><svg viewBox="0 0 12 12"><rect x="1" y="2.5" width="10" height="7"/><path d="M1 2.5l5 4 5-4"/></svg>vik@brlcap.example</li>
    <li><svg viewBox="0 0 12 12"><circle cx="6" cy="6" r="5"/><path d="M1 6h10M6 1c-2.5 3-2.5 7 0 10M6 1c2.5 3 2.5 7 0 10"/></svg>www.brlcap.example</li>
  </ul>
</section>

</body>
</html>
```